Guaranteed Job - Sleek Sexy Business Card UV Spot

Im looking for a sleek and sexy business card, that resembles elite or VIP status status.
our business is corinvale.example
you can view our products on there, but our main audience for handing out our cards will be for people in the hospitality industry, so it will need to impress high management and CEO of hotels and restaurants, bars, clubs etc...
the card features will have UV spot on both sides, 400gsm stock. standard size.
Artwork should be 86 x 54mm + 2mm bleed = 90 x 58mm
it should have a nice "unique" uv spot pattern that highlights the card, not a repeated pattern, theres no originality there, and it will be disregarded.
The written material will be:
Corin Vale Hospitality College (logo)
Tobin Marsh
Director
Phone: 1300 615 737
Mobile: 0455 817 296
Email: info@corinvale.example
website: www.corinvale.example
I'm looking for originality here, i don't want just a simple stock card, want something that has a wow factor for people.
You will find the logo attached. you may invert the white to black words to suit the background as you please.
thank you and good luck
As a side note, ive received a lot of proposals, im too busy to give feedback to each and every one, so if i havent provided feedback for your design within 24 hours, then consider it not acceptable, and you could resubmit another design.
So far i have not seen any design that stood out for me, they all seem pretty generic. there nothing thats unique, i would figure for the amount that im offering, that people would put some more effort and creativity into the design.
so far over 200 designs submitted, and nothing i have seen looks very original, everything looks like a different variation of the same stuff, i said it very clearly i wanted something unique, the only thing that has come close to it so far is this one
Reason: Ive received alot of design concepts and i have reviewed everyone, but i havent had time to give feedback to every single one, only the ones that have interested me, if i havent responded, its because i havent found it good enough.
so far only a few design have been on par with what ive been looking for, an attractive eye popping design.
heres a few of them,
http://files.pixelbazaar.example/design_img/51736/62418/62418_2840915_51736_image.jpg
http://files.pixelbazaar.example/design_img/51736/68254/68254_2841377_51736_image.jpg
theyre, both unique and original, and eye catching, the only thing theyre missing is the sexyness.
if you still think you have some creativity left in your minds, then throw it on here.
Reason: Sorry guys for the delay, I was in a serious accident and out of commission for the past few months, I'm just slowly recovering now, please bare with me as i try to attend to this project, it may take me awhile as I have other projects that are on standby, I'm not 100% at the moment, so im extending the deadline for 2 weeks right now. Thanks for your patience.
Hospitality

```html
<!DOCTYPE html>
<html lang="en">
<head>
<meta charset="utf-8">
<title>Corin Vale Hospitality College – Business Card</title>
<link rel="stylesheet" href="https://fonts.googleapis.com/css2?family=Oswald:wght@500&family=Jost:wght@400;500&display=swap">
<style>
  :root {
    --stage: #e9e6e1;
    --card: #0b0b0c;
    --card-lift: #1a1a1c;
    --teal: #1bb59c;
    --sky: #2ea8e0;
    --brand-blue: #5aaee2;
    --white: #ffffff;
    --soft-grey: #8a8a8d;
    --chevron-grey: #3a3a3c;
    --rule: #2a2a2c;
  }
  * { box-sizing: border-box; margin: 0; padding: 0; }
  html, body { width: 1200px; height: 900px; overflow: hidden; }
  body { background: var(--stage); position: relative; font-family: "Jost", sans-serif; }

  .card {
    position: absolute;
    top: 180px;
    width: 340px;
    height: 540px;
    background: var(--card);
    overflow: hidden;
    box-shadow: 0 10px 30px rgba(0,0,0,.25);
  }
  .card--front { left: 200px; }
  .card--back { left: 660px; }

  .card__texture {
    position: absolute; inset: 0;
    background: radial-gradient(ellipse at 40% 35%, var(--card-lift) 0%, var(--card) 70%);
  }
  .card__shapes { position: absolute; inset: 0; width: 100%; height: 100%; }

  .rule {
    position: absolute; left: 0; width: 100%; height: 2px;
    background: var(--rule);
  }
  .rule--top { top: 95px; }
  .rule--mid { top: 235px; }

  .brand {
    position: absolute;
    font-family: "Oswald", sans-serif;
    font-weight: 500;
    color: var(--white);
    text-transform: uppercase;
    line-height: 1.05;
    display: flex; align-items: center; gap: 12px;
  }
  .brand__mark {
    width: 34px; height: 34px;
    background: var(--brand-blue);
    flex: none;
  }
  .brand__name { font-size: 22px; letter-spacing: .5px; }
  .card--front .brand { left: 46px; top: 138px; }

  .person { position: absolute; left: 46px; top: 268px; }
  .person__name { font-size: 30px; font-weight: 500; color: var(--brand-blue); letter-spacing: .5px; }
  .person__role { font-size: 18px; color: var(--white); margin-top: 2px; }

  .contact {
    position: absolute; left: 46px; top: 352px;
    list-style: none;
    font-size: 13.5px; color: var(--white); line-height: 22px;
  }

  .card--back .brand {
    left: 170px; top: 270px;
    transform: translate(-50%, -50%) rotate(-90deg);
    white-space: nowrap;
  }
  .card--back .brand__name { font-size: 30px; }
  .site {
    position: absolute; left: 232px; top: 270px;
    transform: translate(-50%, -50%) rotate(-90deg);
    font-size: 17px; color: var(--soft-grey); white-space: nowrap; letter-spacing: .5px;
  }
</style>
</head>
<body>

<section class="card card--front" aria-label="Business card front">
  <div class="card__texture" role="img" aria-label="Crumpled gloss UV spot texture across the card"></div>
  <svg class="card__shapes" viewBox="0 0 340 540" aria-hidden="true">
    <path d="M0,48 L62,62 Q78,65 88,52 L130,-5" fill="none" stroke="var(--teal)" stroke-width="14"/>
    <path d="M345,445 L260,430 Q242,427 234,444 L195,545" fill="none" stroke="var(--teal)" stroke-width="26"/>
    <path d="M345,468 L278,458 Q262,456 256,472 L232,545 L345,545 Z" fill="var(--sky)"/>
  </svg>
  <div class="rule rule--top"></div>
  <div class="rule rule--mid"></div>

  <div class="brand">
    <span class="brand__mark"></span>
    <span class="brand__name">Corin Vale<br>Hospitality College</span>
  </div>

  <div class="person">
    <p class="person__name">Tobin Marsh</p>
    <p class="person__role">Director</p>
  </div>

  <ul class="contact">
    <li>Phone: 1300 615 737,</li>
    <li>Mobile: 0455 817 296</li>
    <li>Email: info@corinvale.example</li>
    <li>website: www.corinvale.example</li>
  </ul>
</section>

<section class="card card--back" aria-label="Business card back">
  <div class="card__texture" role="img" aria-label="Crumpled gloss UV spot texture across the card"></div>
  <svg class="card__shapes" viewBox="0 0 340 540" aria-hidden="true">
    <path d="M-5,60 L70,74 Q86,77 94,62 L128,-5" fill="none" stroke="var(--chevron-grey)" stroke-width="16"/>
    <path d="M345,470 L268,456 Q252,453 245,468 L212,545" fill="none" stroke="var(--chevron-grey)" stroke-width="16"/>
  </svg>

  <div class="brand">
    <span class="brand__mark"></span>
    <span class="brand__name">Corin Vale<br>Hospitality College</span>
  </div>
  <p class="site">www.corinvale.example</p>
</section>

</body>
</html>
```